Need to design a business card with logo

Hellow
we are a company ,
PT REKA LINTAS MANDIRI
looking for design of name card.
what we do is property development and management.
design preferable professional corporate look and feel.
corporate. color, pantone colour 289
information required is
company name " Reka Lintas Mandiri"
person name eg " Peter Hollis"
person title eg "secret agent"
address: 9 kestrel road , jakarta, indonesia
phone : +6221 5906471
mobile : 0813 294 615
email : peter@hollistran.com
website: www.peterhol.com
if you want to include logo in the design you are welcome and appreciated , or you can simply use the company name as the logo.
thanks
corporate , business person , show events, exhibition events ,etc
Business

```html
<!DOCTYPE html>
<html lang="en">
<head>
<meta charset="utf-8">
<title>Reka Lintas Mandiri — Business Card</title>
<link rel="stylesheet" href="https://fonts.googleapis.com/css2?family=Mulish:wght@400;700&display=swap">
<style>
  :root {
    --navy: #0c1262;
    --gold: #d9b73c;
    --gold-deep: #b48c24;
    --white: #ffffff;
    --backdrop: #e9e7e3;
  }
  * { margin: 0; padding: 0; box-sizing: border-box; }
  html, body { width: 1200px; height: 1000px; overflow: hidden; }
  body {
    background: var(--backdrop);
    font-family: "Mulish", "Century Gothic", sans-serif;
    position: relative;
  }
  .card {
    position: absolute;
    left: 220px;
    width: 760px;
    height: 440px;
    background: var(--navy);
  }
  .card--front { top: 40px; }
  .card--back { top: 520px; }
  .card__frame {
    position: absolute;
    inset: 22px;
    border: 12px solid var(--gold);
  }

  /* Front */
  .brand-lockup {
    position: absolute;
    left: 0; right: 0;
    top: 170px;
    text-align: center;
  }
  .brand-lockup__name {
    display: inline-flex;
    align-items: center;
    gap: 14px;
    color: var(--white);
    font-size: 36px;
    font-weight: 400;
    letter-spacing: 1px;
  }
  .brand-lockup__mark {
    width: 22px; height: 22px;
    background: var(--gold-deep);
  }
  .brand-lockup__rule {
    width: 440px;
    height: 3px;
    margin: 8px auto 6px;
    background: var(--gold);
  }
  .brand-lockup__tagline {
    color: var(--gold);
    font-size: 20px;
  }

  /* Back */
  .company-name {
    position: absolute;
    left: 72px; top: 78px;
    display: flex; align-items: center; gap: 10px;
    color: var(--white);
    font-weight: 700;
    font-size: 24px;
  }
  .company-name__mark {
    width: 14px; height: 14px;
    background: var(--gold-deep);
  }
  .person {
    position: absolute;
    right: 72px; top: 120px;
    text-align: right;
  }
  .person__name { color: var(--white); font-weight: 700; font-size: 30px; }
  .person__title { color: var(--gold); font-size: 28px; margin-top: 2px; }

  .address {
    position: absolute;
    left: 72px; top: 230px;
    font-size: 26px;
    line-height: 1.22;
  }
  .address__label { color: var(--white); }
  .address__lines { color: var(--gold); }

  .contacts {
    position: absolute;
    right: 60px; top: 262px;
    list-style: none;
    color: var(--gold);
    font-size: 26px;
    line-height: 1.3;
  }
  .contacts__item {
    display: flex; justify-content: flex-end; align-items: center; gap: 12px;
  }
  .contacts__icon { width: 16px; height: 16px; flex: none; }
</style>
</head>
<body>
  <section class="card card--front" aria-label="Card front">
    <div class="card__frame"></div>
    <div class="brand-lockup">
      <div class="brand-lockup__name"><span class="brand-lockup__mark"></span>PT REKA LINTAS MANDIRI</div>
      <div class="brand-lockup__rule"></div>
      <div class="brand-lockup__tagline">property development and management</div>
    </div>
  </section>

  <section class="card card--back" aria-label="Card back">
    <div class="card__frame"></div>
    <div class="company-name"><span class="company-name__mark"></span>Reka Lintas Mandiri</div>
    <div class="person">
      <div class="person__name">Peter Hollis</div>
      <div class="person__title">secret agent</div>
    </div>
    <div class="address">
      <div class="address__label">Address</div>
      <div class="address__lines">9 kestrel road ,<br>jakarta,<br>indonesia</div>
    </div>
    <ul class="contacts">
      <li class="contacts__item">+6221 5906471
        <svg class="contacts__icon" viewBox="0 0 16 16" fill="#fff"><path d="M3 1l3 3-1.5 2c1 2 3 4 5 5L11.5 9.5l3 3-2 2.5C6 14 2 10 1 3z"/></svg></li>
      <li class="contacts__item">0813 294 615
        <svg class="contacts__icon" viewBox="0 0 16 16" fill="none" stroke="#fff" stroke-width="1.4"><rect x="4.5" y="1" width="7" height="14" rx="1.2"/><line x1="7" y1="12.5" x2="9" y2="12.5"/></svg></li>
      <li class="contacts__item">peter@hollistran.com
        <svg class="contacts__icon" viewBox="0 0 16 16" fill="none" stroke="#fff" stroke-width="1.4"><rect x="1" y="3.5" width="14" height="9"/><path d="M1 3.5l7 5 7-5"/></svg></li>
      <li class="contacts__item">www.peterhol.com
        <svg class="contacts__icon" viewBox="0 0 16 16" fill="none" stroke="#fff" stroke-width="1.2"><circle cx="8" cy="8" r="6.5"/><ellipse cx="8" cy="8" rx="3" ry="6.5"/><line x1="1.5" y1="8" x2="14.5" y2="8"/></svg></li>
    </ul>
  </section>
</body>
</html>
```